female esthetician looking for an impact business card

I an an expert in skin care industry with high experience in NYC.I want my business card to look professional , an impact at first look. I do want a combination between white and gold . I believe the font will be great if is gold.. The Fonts are also important. MIRELA COSTANDI (SKIN CARE BOUTIQUE)

THIS SHOULD BE THE BUSINESS NAME, and should be placed on th eback of the card.
IN front m, the name MIRELA COSTANDI - ESTHETCIAN

BY APPOINTMENTS ONLY: 512.478.2936

Target Market(s)

HIGH END CLIENTELE

Contact Information for Business Card

iT WILL BE on a luxury paper. I neeed the wow feeling

Requirements
Should not have
• pictures

```html
<!DOCTYPE html>
<html lang="en">
<head>
<meta charset="utf-8">
<title>Mirela Costandi – Business Card</title>
<link rel="stylesheet" href="https://fonts.googleapis.com/css2?family=Great+Vibes&family=Lato:wght@400&display=swap">
<style>
  :root {
    --backdrop: #e4e3df;
    --paper: #f6f5f1;
    --band: #3a302c;
    --gold: #c29a3c;
    --ink: #1f1c1a;
  }
  html, body {
    margin: 0;
    padding: 0;
    width: 1200px;
    height: 801px;
    overflow: hidden;
    background: var(--backdrop);
  }
  .canvas {
    position: relative;
    width: 1200px;
    height: 801px;
    display: flex;
    align-items: center;
    justify-content: center;
  }
  .card {
    position: relative;
    width: 400px;
    height: 700px;
    background: var(--paper);
    box-shadow: 0 2px 10px rgba(0,0,0,0.12);
    overflow: hidden;
  }
  .card__band {
    position: absolute;
    left: 0;
    width: 100%;
    height: 92px;
    background: var(--band);
  }
  .card__band--top { top: 0; }
  .card__band--bottom { bottom: 0; }
  .card__brand {
    position: absolute;
    top: 175px;
    left: 0;
    width: 100%;
    text-align: center;
    font-family: "Great Vibes", cursive;
    font-size: 78px;
    color: var(--gold);
    line-height: 1;
  }
  .card__name {
    position: absolute;
    top: 330px;
    left: 0;
    width: 100%;
    text-align: center;
    font-family: "Great Vibes", cursive;
    font-size: 50px;
    color: var(--ink);
    line-height: 1;
  }
  .card__contact {
    position: absolute;
    top: 430px;
    left: 0;
    width: 100%;
    text-align: center;
    font-family: "Lato", sans-serif;
    font-size: 17px;
    color: var(--ink);
    line-height: 1.55;
    letter-spacing: 0.02em;
  }
  .card__contact p { margin: 0; }
</style>
</head>
<body>
  <main class="canvas">
    <article class="card">
      <div class="card__band card__band--top" role="img" aria-label="Dark brown band with gold swirl flourishes"></div>
      <div class="card__brand">Costandi</div>
      <h1 class="card__name">Mirela Costandi</h1>
      <div class="card__contact">
        <p class="card__phone">512.478.2936</p>
        <p class="card__email">hello@costandiskin.com</p>
      </div>
      <div class="card__band card__band--bottom" role="img" aria-label="Dark brown band with gold swirl flourishes"></div>
    </article>
  </main>
</body>
</html>
```